Consulting company with focus on aviation needs

We need a new business card design for our company. The company consults with multiple players in the industry like manufacturers and airlines. It is also a supplier and an inter-company level. Given the targeted industry (aviation) it should be both kind of serious, sound, secure, classy, ​​but also a bit technical, innovative. Should not be too playful, however, "fresh", "airy", "ligth" and "suprising" are suitabe attributes. The existing logo shall be used.

Airlines

```html
<!DOCTYPE html>
<html lang="en">
<head>
<meta charset="utf-8">
<title>Velaris Business Card</title>
<link href="https://fonts.googleapis.com/css2?family=Arimo:wght@400;700&display=swap" rel="stylesheet">
<style>
  :root {
    --stage: #e4e4e4;
    --card: #2a2a2c;
    --wordmark: #8d8f91;
    --orange: #e8922a;
    --teal: #0a9a80;
    --green: #7cb35a;
    --grey: #65696a;
    --muted: #8a8a8a;
    --white: #ffffff;
  }
  * { margin: 0; padding: 0; box-sizing: border-box; }
  html, body {
    width: 799px; height: 1200px; overflow: hidden;
    background: var(--stage);
    font-family: "Arimo", Arial, sans-serif;
  }
  .canvas { position: relative; width: 799px; height: 1200px; }
  .card {
    position: absolute; left: 240px; width: 320px; height: 540px;
    background: var(--card); overflow: hidden;
    box-shadow: 0 6px 18px rgba(0,0,0,.25);
  }
  .card--front { top: 40px; }
  .card--back { top: 620px; }

  .wordmark { font-weight: 400; color: var(--wordmark); letter-spacing: 7px; line-height: 1; white-space: nowrap; }
  .tagline { color: var(--orange); font-size: 12px; margin-top: 6px; white-space: nowrap; }

  /* front */
  .front-disc {
    position: absolute; left: -20px; top: 30px;
    width: 330px; height: 330px; border-radius: 50%;
    background: var(--grey);
  }
  .front-brand { position: absolute; right: 28px; bottom: 36px; }
  .front-brand .wordmark { font-size: 40px; }

  /* back */
  .brand-dot {
    position: absolute; left: 30px; top: 40px;
    width: 62px; height: 62px; border-radius: 50%; background: var(--grey);
  }
  .back-brand { position: absolute; left: 30px; top: 118px; }
  .back-brand .wordmark { font-size: 34px; letter-spacing: 6px; }

  .person { position: absolute; left: 64px; top: 196px; }
  .person-name { color: var(--teal); font-size: 21px; }
  .person-role { color: var(--muted); font-size: 12px; margin-top: 4px; }

  .divider { position: absolute; left: 64px; width: 200px; height: 1px; background: var(--orange); }
  .divider--one { top: 250px; }
  .divider--two { top: 372px; }

  .contacts { position: absolute; left: 64px; top: 264px; color: var(--muted); font-size: 12px; line-height: 1.75; }
  .icons { display: flex; gap: 6px; margin-bottom: 4px; }
  .icons svg { width: 13px; height: 13px; }
  .web-accent { color: var(--green); }

  .address { position: absolute; left: 64px; top: 386px; color: var(--muted); font-size: 12px; line-height: 1.75; }

  .company-band {
    position: absolute; left: 0; bottom: 0; width: 100%; height: 48px;
    background: linear-gradient(90deg, var(--green), var(--teal));
    display: flex; align-items: center; padding-left: 30px;
  }
  .company-band span { color: var(--white); font-size: 15px; letter-spacing: .5px; }
</style>
</head>
<body>
<main class="canvas">

  <section class="card card--front">
    <div class="front-disc" aria-hidden="true"></div>
    <div class="front-brand">
      <div class="wordmark">VELARIS</div>
      <div class="tagline">Linking Partners - Shaping Flight</div>
    </div>
  </section>

  <section class="card card--back">
    <div class="brand-dot" aria-hidden="true"></div>
    <div class="back-brand">
      <div class="wordmark">VELARIS</div>
      <div class="tagline">Linking Partners - Shaping Flight</div>
    </div>

    <div class="person">
      <div class="person-name">John K. Smith</div>
      <div class="person-role">Managing Director</div>
    </div>

    <div class="divider divider--one"></div>

    <div class="contacts">
      <div class="icons">
        <svg viewBox="0 0 14 14" aria-label="phone"><path fill="#e8922a" d="M3 1l2 0 1 3-1.5 1a7 7 0 0 0 4.5 4.5L10 8l3 1v2a2 2 0 0 1-2 2A10 10 0 0 1 1 3a2 2 0 0 1 2-2z"/></svg>
        <svg viewBox="0 0 14 14" aria-label="email"><rect x="1" y="3" width="12" height="8" fill="#e8922a"/><path d="M1 3l6 5 6-5" stroke="#2a2a2c" fill="none"/></svg>
        <svg viewBox="0 0 14 14" aria-label="website"><circle cx="7" cy="7" r="5.5" fill="none" stroke="#e8922a" stroke-width="1.5"/><path d="M1.5 7h11M7 1.5c-3 3-3 8 0 11M7 1.5c3 3 3 8 0 11" stroke="#e8922a" fill="none"/></svg>
      </div>
      <div>+00-112-223-3344</div>
      <div>name@yourwebsite.com</div>
      <div>www.<span class="web-accent">yourwebsite</span>.com</div>
    </div>

    <div class="divider divider--two"></div>

    <div class="address">
      <div>123, Street No. 6, City Name</div>
      <div>Opp. Country 123456</div>
    </div>

    <div class="company-band"><span>VELARIS PVT LTD.</span></div>
  </section>

</main>
</body>
</html>
```